Private London College Prospectus

A single spread to begin with followed by treatments for a couple of awkward spreads in the brochure. Attached docs include previous few years to show how the design has evolved. We're now looking for a different direction
Outline: Private college in Central London.
Mainly A-levels but also GCSE courses
Consistently at the top of London results table
Operated by the owners
Prospectus is sent to anyone enquiring about the college

Target Market(s)

High net worth families in the Uk and abroad

Industry/Entity Type

College

Requirements
Must have
• Modern fonts
• House colour is purple - PMS 8804
• Teacher quote
• Page quote
Nice to have
• See attachments - the gryphon is part of their logo but not essential
Should not have
• Shouldn't be too fussy or cluttered
• No script fonts (probably) no italics in main text

```html
<!DOCTYPE html>
<html lang="en">
<head>
<meta charset="utf-8">
<title>Halbridge College – Prospectus Spread</title>
<link href="https://fonts.googleapis.com/css2?family=Catamaran:wght@400;500;600;700&display=swap" rel="stylesheet">
<style>
  :root {
    --purple: #6a1b63;
    --purple-deep: #521449;
    --purple-bright: #8a2c84;
    --ink: #1a1a1a;
    --paper: #ffffff;
    --backdrop: #e4e4e4;
    --photo-warm: #8a5a44;
    --photo-skin: #b89280;
  }
  * { margin: 0; padding: 0; box-sizing: border-box; }
  html, body { width: 1200px; height: 849px; overflow: hidden; background: var(--backdrop); }
  .spread {
    position: relative; width: 1200px; height: 849px; overflow: hidden;
    background: var(--paper);
    font-family: "Catamaran", sans-serif; color: var(--ink);
  }
  .fold {
    position: absolute; left: 540px; top: 0; width: 120px; height: 849px;
    background: linear-gradient(90deg, rgba(0,0,0,0) 0%, rgba(0,0,0,0.05) 50%, rgba(0,0,0,0) 100%);
    pointer-events: none; z-index: 5;
  }
  .shapes { position: absolute; inset: 0; }
  .footer-band {
    position: absolute; left: 0; bottom: 0; width: 100%; height: 30px;
    background: linear-gradient(90deg, #000 0%, #222 50%, #000 100%);
  }

  /* Left page */
  .wordmark {
    position: absolute; left: 382px; top: 46px; width: 196px; height: 78px;
    background: var(--purple);
    display: flex; align-items: center; justify-content: center;
  }
  .wordmark span { color: var(--paper); font-size: 34px; font-weight: 500; letter-spacing: -0.5px; }
  .ethos {
    position: absolute; left: 369px; top: 225px; width: 214px;
    color: var(--paper); font-size: 16px; font-weight: 500; line-height: 22px; letter-spacing: -0.4px;
  }
  .ethos .line { display: block; white-space: nowrap; text-align: justify; text-align-last: justify; }
  .ethos .line.last { text-align-last: left; }
  .page-quote {
    position: absolute; left: 318px; top: 505px; width: 262px;
    font-size: 20px; font-weight: 500; line-height: 31px;
  }
  .page-quote .first { display: block; color: var(--purple); }
  .page-quote .second { display: block; text-align: right; color: var(--ink); }
  .section-title {
    color: var(--purple); font-size: 23px; font-weight: 600; line-height: 30px;
  }
  .body-copy p {
    font-size: 12.8px; line-height: 17.4px; text-align: justify; letter-spacing: -0.1px;
  }
  .why { position: absolute; left: 28px; top: 597px; width: 545px; }
  .why .body-copy { margin-top: 6px; }
  .why .body-copy p + p { margin-top: 17px; }

  /* Right page */
  .teacher-quote {
    position: absolute; right: 29px; top: 30px; width: 560px; text-align: right;
  }
  .teacher-quote .label { color: var(--purple); font-size: 25px; font-weight: 600; line-height: 30px; }
  .teacher-quote .name { color: var(--ink); font-size: 22px; font-weight: 600; line-height: 30px; }
  .teacher-quote .role { color: var(--purple); font-size: 25px; font-weight: 400; line-height: 30px; }
  .teacher-quote blockquote { font-size: 12.8px; line-height: 17px; margin-top: 8px; }
  .best { position: absolute; left: 622px; top: 497px; width: 552px; }
  .best .section-title { width: 240px; font-size: 24px; line-height: 31px; }
  .best .body-copy { margin-top: 6px; }
  .best .body-copy p + p { margin-top: 13px; }

  .photo-frame {
    position: absolute; left: 619px; top: 207px; width: 561px; height: 225px;
    background: var(--paper); border-radius: 3px; padding: 3px 3px 0;
    box-shadow: 0 1px 3px rgba(0,0,0,0.2);
  }
  .photo {
    background: linear-gradient(120deg, var(--photo-warm), #5c3426 55%, var(--photo-skin));
  }
  .photo-frame .photo { width: 100%; height: 190px; }
</style>
</head>
<body>
<div class="spread">
  <svg class="shapes" width="1200" height="849" viewBox="0 0 1200 849" xmlns="http://www.w3.org/2000/svg">
    <defs>
      <linearGradient id="band" x1="0" y1="0" x2="1" y2="0">
        <stop offset="0" stop-color="#4f1347"/>
        <stop offset="0.5" stop-color="#6a1b63"/>
        <stop offset="1" stop-color="#8a2c84"/>
      </linearGradient>
      <linearGradient id="groupPhoto" x1="0" y1="0" x2="1" y2="1">
        <stop offset="0" stop-color="#3b3a3c"/>
        <stop offset="0.5" stop-color="#7d6a63"/>
        <stop offset="1" stop-color="#2b2f3a"/>
      </linearGradient>
      <linearGradient id="portraitA" x1="0" y1="0" x2="0" y2="1">
        <stop offset="0" stop-color="#d9d6d0"/>
        <stop offset="1" stop-color="#4a2a6b"/>
      </linearGradient>
      <linearGradient id="portraitB" x1="0" y1="0" x2="1" y2="1">
        <stop offset="0" stop-color="#c9b59a"/>
        <stop offset="1" stop-color="#7d7c80"/>
      </linearGradient>
    </defs>

    <!-- purple band and rule -->
    <rect x="150" y="179" width="1050" height="285" fill="url(#band)"/>
    <rect x="315" y="475" width="885" height="2" fill="var(--purple)"/>

    <!-- large group portrait -->
    <circle cx="117" cy="338" r="248" fill="#111"/>
    <circle cx="110" cy="330" r="246" fill="var(--purple)"/>
    <circle cx="110" cy="330" r="238" fill="var(--paper)"/>
    <circle cx="110" cy="330" r="232" fill="url(#groupPhoto)" role="img" aria-label="Photograph of a group of smiling sixth-form students"/>

    <!-- small portraits -->
    <circle cx="933" cy="494" r="80" fill="var(--purple)"/>
    <circle cx="933" cy="494" r="73" fill="var(--paper)"/>
    <circle cx="933" cy="494" r="68" fill="url(#portraitA)" role="img" aria-label="Photograph of a student in a purple hoodie"/>
    <circle cx="1096" cy="494" r="80" fill="var(--purple)"/>
    <circle cx="1096" cy="494" r="73" fill="var(--paper)"/>
    <circle cx="1096" cy="494" r="68" fill="url(#portraitB)" role="img" aria-label="Photograph of a student studying a molecular model"/>
  </svg>

  <div class="wordmark"><span>Halbridge</span></div>

  <p class="ethos">
    <span class="line last">The Halbridge Ethos</span>
    <span class="line">Based in the heart of Mayfair in</span>
    <span class="line">central London, Halbridge is a</span>
    <span class="line">top performing independent</span>
    <span class="line">sixth-form college, offering a</span>
    <span class="line">broad A-level and GCSE</span>
    <span class="line">curriculum for students from</span>
    <span class="line">public, state and private school</span>
    <span class="line last">backgrounds</span>
  </p>

  <p class="page-quote"><span class="first">“a modern college with...</span><span class="second">... a traditional approach”</span></p>

  <section class="why">
    <h2 class="section-title">Why Choose Halbridge?</h2>
    <div class="body-copy">
      <p>The majority of students who come to Halbridge do so because of our reputation for excellent A-level and GCSE results. This is true of students both on our full two-year programme, as well as those on the one-year intensive programme. Most students will progress on to a top 20 UK university.</p>
      <p>Students are taught very much by traditional methods, in small groups, concentrating on the skills needed to pass examinations and to be successful at university. All teachers at Halbridge are subject specialists and most have experience as examiners. They are particularly successful with young people: they are able to motivate and communicate with them in ways which they understand. Barriers are quickly broken down, enhancing the learning process</p>
    </div>
  </section>

  <section class="teacher-quote">
    <h2 class="label">TEACHER QUOTE</h2>
    <p class="name">ARJUN MALHOTRA</p>
    <p class="role">Head of Economics</p>
    <blockquote>We teach students how to develop their powers of analysis and independence of thought - crucial to success at university and beyond.</blockquote>
  </section>

  <div class="photo-frame">
    <div class="photo" role="img" aria-label="Photograph of three students seated together in a wood-panelled room"></div>
  </div>

  <section class="best">
    <h2 class="section-title">How Do We Get The Best Out Of Our Students?</h2>
    <div class="body-copy">
      <p>Students benefit from individually tailored attention outside of classes – a key element of our successful A-level and GCSE programmes, and at Halbridge each student has a Curriculum Manager and a Personal Tutor, who provide advice on study skills, subject choices and careers, and who also monitor progress in regular meetings with students.</p>
      <p>We expect full commitment from our students and as such we have strict rules on attendance and timely submission of assignments. Parents are able to monitor progress through monthly reports, easily accessible using our online reporting system. Parents’ Evenings are held during the Autumn and Spring terms.</p>
      <p>We encourage our students every step of the way and we help them to build confidence through examination success. We see the learning process as a successful partnership between students, tutors and parents.</p>
    </div>
  </section>

  <div class="footer-band"></div>
  <div class="fold"></div>
</div>
</body>
</html>
```